ink nest studio nos proporciona ter várias ideias vindo de mentes criativas diferentes o que nos faz termos muito mais variedades do que se uma única pessoa criasse vários logos.

```html
<!DOCTYPE html>
<html lang="pt-BR">
<head>
<meta charset="utf-8">
<title>Lume Produções — cartão de visita</title>
<link href="https://fonts.googleapis.com/css2?family=Montserrat:wght@400;600;800&display=swap" rel="stylesheet">
<style>
  :root {
    --bg: #2b2d30;
    --card: #ffffff;
    --ink: #2a2a2a;
    --muted: #6b6b6b;
    --blue: #9fd4f0;
    --green: #a6e59a;
    --pink: #f39cae;
    --yellow: #f5ef8c;
    --purple: #e0a6ea;
    --teal: #27b3b8;
    --mint: #5cc46a;
    --rose: #e2336f;
    --sun: #f2d21b;
  }
  * { box-sizing: border-box; margin: 0; padding: 0; }
  html, body { width: 1200px; height: 1200px; overflow: hidden; }
  body {
    background: var(--bg);
    font-family: "Montserrat", sans-serif;
    display: flex;
    flex-direction: column;
    align-items: center;
    justify-content: center;
    gap: 70px;
  }
  .card {
    position: relative;
    width: 900px;
    height: 500px;
    background: var(--card);
    border-radius: 30px;
    overflow: hidden;
  }
  /* Back face: soft pastel edge strips */
  .edge {
    position: absolute;
    left: 0; right: 0;
    height: 62px;
    background: linear-gradient(90deg, var(--blue), var(--green), var(--pink), var(--yellow), var(--purple));
    opacity: 0.85;
  }
  .edge--top { top: 0; }
  .edge--bottom { bottom: 0; }

  .brand {
    display: flex;
    align-items: center;
    gap: 18px;
    color: var(--ink);
    font-weight: 800;
    letter-spacing: 1px;
    white-space: nowrap;
  }
  .brand__mark { flex: none; background: var(--pink); border-radius: 4px; }
  .card--back .brand {
    position: absolute;
    left: 50%; top: 50%;
    transform: translate(-50%, -50%);
    font-size: 46px;
  }
  .card--back .brand__mark { width: 46px; height: 46px; }

  /* Front face: identity and contacts */
  .card--front .brand {
    position: absolute;
    left: 60px; top: 204px;
    font-size: 28px;
  }
  .card--front .brand__mark { width: 30px; height: 30px; }
  .person {
    position: absolute;
    left: 480px; top: 80px;
  }
  .person__name { font-size: 38px; font-weight: 800; color: var(--ink); }
  .person__role { font-size: 20px; color: var(--muted); margin-top: 4px; }
  .contacts {
    list-style: none;
    position: absolute;
    left: 480px; top: 210px;
    display: flex;
    flex-direction: column;
    gap: 22px;
  }
  .contact {
    display: flex;
    align-items: center;
    gap: 18px;
    font-size: 19px;
    color: var(--muted);
    line-height: 1.3;
  }
  .contact svg { flex: none; width: 34px; height: 34px; }
</style>
</head>
<body>

  <section class="card card--back" aria-label="Verso do cartão">
    <div class="edge edge--top" role="img" aria-label="Faixa decorativa em tons pastel"></div>
    <div class="brand"><span class="brand__mark"></span>LUME PRODUÇÕES</div>
    <div class="edge edge--bottom" role="img" aria-label="Faixa decorativa em tons pastel"></div>
  </section>

  <section class="card card--front" aria-label="Frente do cartão">
    <div class="brand"><span class="brand__mark"></span>LUME PRODUÇÕES</div>
    <div class="person">
      <p class="person__name">Nome Sobrenome</p>
      <p class="person__role">Cargo</p>
    </div>
    <ul class="contacts">
      <li class="contact">
        <svg viewBox="0 0 34 34"><circle cx="17" cy="17" r="17" fill="var(--teal)"/><path d="M17 8a6 6 0 0 0-6 6c0 5 6 12 6 12s6-7 6-12a6 6 0 0 0-6-6zm0 8.2a2.2 2.2 0 1 1 0-4.4 2.2 2.2 0 0 1 0 4.4z" fill="#fff"/></svg>
        <span>R. Sua Rua, nº 00, Cidade - XX<br>CEP 00000-000</span>
      </li>
      <li class="contact">
        <svg viewBox="0 0 34 34"><circle cx="17" cy="17" r="17" fill="var(--mint)"/><rect x="9" y="11" width="16" height="12" rx="1.5" fill="#fff"/><path d="M9.5 11.5 17 18l7.5-6.5" stroke="var(--mint)" stroke-width="1.6" fill="none"/></svg>
        <span>seuemail@mail.com</span>
      </li>
      <li class="contact">
        <svg viewBox="0 0 34 34"><circle cx="17" cy="17" r="17" fill="var(--rose)"/><circle cx="17" cy="17" r="8" stroke="#fff" stroke-width="1.8" fill="none"/><path d="M9 17h16M17 9c-3.5 4-3.5 12 0 16M17 9c3.5 4 3.5 12 0 16" stroke="#fff" stroke-width="1.5" fill="none"/></svg>
        <span>www.seusite.com.br</span>
      </li>
      <li class="contact">
        <svg viewBox="0 0 34 34"><circle cx="17" cy="17" r="17" fill="var(--sun)"/><path d="M12 9.5l3 .5 1.5 4-2 1.5a10 10 0 0 0 4.5 4.5l1.5-2 4 1.5.5 3c-1 1.5-3 2-5 1.2A15 15 0 0 1 10.8 14.5C10 12.5 10.5 10.5 12 9.5z" fill="#fff"/></svg>
        <span>(00) 99999-9999<br>(00) 8888-8888</span>
      </li>
    </ul>
  </section>

</body>
</html>
```